Business Card Design for an international medical business

We need a professional and elegant business card design with fashionable graphic element. Our company is located in Hong Kong with three worldwide production lines for medical equipment(surgical face masks, N95, face shields and so on). Our factories all contain medical standard ISOs and all product fulfill Garrow lab and KTR testing standards.

We would like to see designs that show the impression of our professional expertise, formal corporate image with creative thinking work style and inspiring global concept. We want the content in both English and Japanese on the same card. We also want to print our the patent trade mark and company logo on the card.

Target Market(s)

Southeast Asia, US, EU

Industry/Entity Type

Medical Equipment

Contact Information for Business Card

Below are the content we want to be shown on the business card(please help us to simplified them to be more presentable and readable):

Company name: Brightmoor (Hong Kong) 5K Medical Technology Company Limited
Address: Unit 2204, 22/F, Pine Court, No.8 Ferndale Road, Kwun Lam, Hong Kong.
Band Name: B5K
Homepage: www.brightmoor5kq.com
Name: Lok Wing Fei
Title: Manager
Tel: +852-xxxx-xxxx
Mobile: +852-xxxx-xxxx
Email: xx@brightmoor5kq.com

Production Lines:
China: Ping Shan Kai Lok Medical Technology Company Limited
Mo Tan City Ren Bo Textile Machinery Company Limited
Bangladesh: B5K Medical Technology Company Limited

Qualifications:
ISO 13485:2016
ISO 14644-1:2015
ISO Class 8 Cleanroom
ASTM F2100 Level 2
EN14683 Type IIR
EN149 FFP2
CE Certified
FDA Registration number: XXX

Requirements
Must have
• use pantone color for the design
and provide the pantone number for printing purpose
Should not have
• Background color should not be black.

```html
<!DOCTYPE html>
<html lang="en">
<head>
<meta charset="utf-8">
<title>Brightmoor Business Card</title>
<link rel="stylesheet" href="https://fonts.googleapis.com/css2?family=Roboto:wght@400;500;700&display=swap">
<style>
  :root {
    --pink: #e0064f;
    --teal: #17a9a6;
    --ink: #2b2b2b;
    --card: #f4f4f4;
    --card-edge: #e6e6e6;
    --backdrop: #b9b9b9;
  }
  * { box-sizing: border-box; margin: 0; padding: 0; }
  html, body { width: 1200px; height: 576px; overflow: hidden; }
  body {
    background: var(--backdrop);
    font-family: "Roboto", Arial, sans-serif;
    color: var(--ink);
    position: relative;
  }
  .card {
    position: absolute;
    width: 484px;
    height: 292px;
    border-radius: 12px;
    background: linear-gradient(180deg, #f7f7f7 0%, var(--card) 60%, var(--card-edge) 100%);
    overflow: hidden;
    box-shadow: 2px 4px 6px rgba(0,0,0,0.25);
  }
  .card--back { left: 82px; top: 139px; }
  .card--front { left: 602px; top: 138px; width: 480px; }

  /* Back side */
  .section-head {
    position: absolute;
    left: 23px;
    width: 438px;
    height: 22px;
    display: flex;
    align-items: center;
  }
  .section-head__pill {
    background: var(--pink);
    color: #fff;
    font-weight: 500;
    font-size: 12.5px;
    padding: 0 11px;
    height: 22px;
    line-height: 22px;
    border-radius: 11px;
    white-space: nowrap;
  }
  .section-head__rule { flex: 1; height: 1.5px; background: var(--teal); }
  .section-head--lines { top: 36px; }
  .section-head--quals { top: 156px; }

  .flag {
    position: absolute;
    left: 34px;
    width: 40px;
    height: 24px;
  }
  .flag--bangladesh { top: 71px; background: #0a6b3e; }
  .flag--china { top: 105px; background: #de2910; }

  .plant {
    position: absolute;
    left: 92px;
    font-size: 13px;
    line-height: 20px;
    white-space: nowrap;
  }
  .plant--bd { top: 71px; }
  .plant--cn { top: 102px; }

  .quals {
    position: absolute;
    left: 32px;
    top: 190px;
    font-size: 13px;
    line-height: 21px;
    white-space: nowrap;
  }
  .quals .sep { color: var(--pink); margin: 0 5px; }

  .site {
    position: absolute;
    left: 32px;
    top: 251px;
    font-size: 12.5px;
  }
  .site .accent { color: var(--teal); }

  .footer-band {
    position: absolute;
    left: 0; bottom: 0;
    width: 100%;
    height: 9px;
    background: var(--teal);
  }
  .fda {
    position: absolute;
    right: 0; bottom: 0;
    width: 260px;
    height: 37px;
    background: var(--pink);
    clip-path: polygon(14px 0, 100% 0, 100% 100%, 0 100%);
    color: #fff;
    font-size: 12.5px;
    line-height: 37px;
    text-align: right;
    padding-right: 23px;
  }

  /* Front side */
  .side-bar {
    position: absolute;
    left: 0; top: 0;
    width: 44px; height: 100%;
    background: var(--pink);
  }
  .side-rule {
    position: absolute;
    left: 52px; top: 0;
    width: 3px; height: 100%;
    background: var(--teal);
  }
  .brand {
    position: absolute;
    left: 74px;
    top: 40px;
    display: flex;
    align-items: center;
    gap: 10px;
  }
  .brand__dot {
    width: 16px; height: 16px;
    border-radius: 50%;
    background: var(--pink);
  }
  .brand__name {
    font-weight: 700;
    font-size: 34px;
    letter-spacing: 0.5px;
    color: var(--pink);
    line-height: 40px;
  }
  .brand__tagline {
    position: absolute;
    left: 100px;
    top: 80px;
    font-size: 9.5px;
    font-weight: 500;
    color: var(--teal);
  }
  .person__name {
    position: absolute;
    left: 74px;
    top: 125px;
    font-size: 21px;
    font-weight: 500;
    color: var(--teal);
  }
  .person__title {
    position: absolute;
    left: 74px;
    top: 151px;
    font-size: 12px;
  }
  .contact {
    position: absolute;
    display: flex;
    align-items: center;
    gap: 8px;
    font-size: 12.5px;
    white-space: nowrap;
  }
  .contact svg { width: 12px; height: 12px; flex: none; fill: var(--pink); }
  .contact--tel1 { left: 76px; top: 186px; }
  .contact--tel2 { left: 76px; top: 206px; }
  .contact--mail { left: 212px; top: 186px; }
  .contact--web  { left: 212px; top: 206px; }
  .contact--addr { left: 76px; top: 234px; align-items: flex-start; line-height: 18px; }
  .contact--addr svg { margin-top: 2px; }
</style>
</head>
<body>

<section class="card card--back">
  <div class="section-head section-head--lines">
    <span class="section-head__pill">Our Production Lines</span>
    <span class="section-head__rule"></span>
  </div>
  <div class="flag flag--bangladesh" role="img" aria-label="Flag of Bangladesh"></div>
  <p class="plant plant--bd">B5K Medical Technology Company Limited</p>
  <div class="flag flag--china" role="img" aria-label="Flag of China"></div>
  <p class="plant plant--cn">Ping Shan Kai Lok Medical Technology Company Limited<br>Mo Tan City Ren Bo Textile Machinery Company Limited</p>

  <div class="section-head section-head--quals">
    <span class="section-head__pill">Our Qualifications</span>
    <span class="section-head__rule"></span>
  </div>
  <p class="quals">
    ISO 13485:2016<span class="sep">|</span>ISO 14644-1:2015<span class="sep">|</span>ISO Class 8 Cleanroom<br>
    ASTM F2100 Level 2<span class="sep">|</span>EN14683 Type IIR<span class="sep">|</span>EN149 FFP2<span class="sep">|</span>CE Certified
  </p>

  <p class="site">www.<span class="accent">brightmoor5kq</span>.com</p>
  <div class="footer-band"></div>
  <div class="fda">FDA Registration number: 12345</div>
</section>

<section class="card card--front">
  <div class="side-bar"></div>
  <div class="side-rule"></div>

  <div class="brand">
    <span class="brand__dot"></span>
    <span class="brand__name">BRIGHTMOOR</span>
  </div>
  <p class="brand__tagline">5K Medical Technology Company Limited</p>

  <h1 class="person__name">Lok Wing Fei</h1>
  <p class="person__title">Manager</p>

  <p class="contact contact--tel1">
    <svg viewBox="0 0 24 24" aria-hidden="true"><path d="M6.6 10.8a15.5 15.5 0 0 0 6.6 6.6l2.2-2.2c.3-.3.7-.4 1-.2 1.1.4 2.3.6 3.6.6.6 0 1 .4 1 1V20c0 .6-.4 1-1 1A17 17 0 0 1 3 4c0-.6.4-1 1-1h3.5c.6 0 1 .4 1 1 0 1.3.2 2.5.6 3.6.1.3 0 .7-.2 1z"/></svg>
    +852-0000-0000
  </p>
  <p class="contact contact--tel2">
    <svg viewBox="0 0 24 24" aria-hidden="true"><path d="M6.6 10.8a15.5 15.5 0 0 0 6.6 6.6l2.2-2.2c.3-.3.7-.4 1-.2 1.1.4 2.3.6 3.6.6.6 0 1 .4 1 1V20c0 .6-.4 1-1 1A17 17 0 0 1 3 4c0-.6.4-1 1-1h3.5c.6 0 1 .4 1 1 0 1.3.2 2.5.6 3.6.1.3 0 .7-.2 1z"/></svg>
    +852-0000-0000
  </p>
  <p class="contact contact--mail">
    <svg viewBox="0 0 24 24" aria-hidden="true"><path d="M2 5h20v14H2z M2 5l10 8 10-8" fill="var(--pink)"/><path d="M2 5l10 8 10-8" fill="none" stroke="#fff" stroke-width="1.6"/></svg>
    lok@brightmoor5kq.com
  </p>
  <p class="contact contact--web">
    <svg viewBox="0 0 24 24" aria-hidden="true"><circle cx="12" cy="12" r="10"/><path d="M2 12h20M12 2c3 3 3 17 0 20M12 2c-3 3-3 17 0 20" fill="none" stroke="#fff" stroke-width="1.4"/></svg>
    www.brightmoor5kq.com
  </p>
  <p class="contact contact--addr">
    <svg viewBox="0 0 24 24" aria-hidden="true"><path d="M12 2a7 7 0 0 0-7 7c0 5 7 13 7 13s7-8 7-13a7 7 0 0 0-7-7zm0 9.5A2.5 2.5 0 1 1 12 6.5a2.5 2.5 0 0 1 0 5z"/></svg>
    <span>Unit 2204, 22/F, Pine Court,<br>No.8 Ferndale Road, Kwun Lam, Hong Kong.</span>
  </p>
</section>

</body>
</html>
```